Ma V's -100% Juice -Can Design - 8 Varieties

We are looking for to design our new range of 100% Juices which are made in Vietnam and will be imported into Australia.
Our New Brand is to be called “Ma V’s” or "Ma V's Juices"
We will initially have 8 products in the range. Our range of 100% juices will be packed in 500ml Aluminium Cans.
We envisage to have the same general/consistent branding on each can but with different fruit images of all the different juice varieties to be a main part for the image. I have attached a couple of samples of Juice design so you can use a reference point.
We will have the following varieties in our Juice range:
Pineapple
Mango
Passion fruit
Lychee
Pink Guava
Watermelon
Coconut Water
Coconut Water with Chocolate
We have done a few designs for the branding of "Ma V’s” which are attached below but we are happy if they are modified/adjusted to fit in with the overall design of the can.
The design needs to state:
“100% Natural”
“No Added Sugar”
“Never from Concentrate”
“Made from Whole fruit”
The back of the can will need a Nutritional Panel, Ingredient list and must have a barcode.
Image below attached with requirements needed for Australia.
The cans must look striking so they stand out and elegant and sophisticated.

```html
<!DOCTYPE html>
<html lang="en">
<head>
<meta charset="utf-8">
<title>Ma V's Juice Range</title>
<link rel="stylesheet" href="https://fonts.googleapis.com/css2?family=Josefin+Sans:wght@300;400;700&family=Montserrat:wght@400;500;600&family=Fredoka:wght@600&family=Federo&display=swap">
<style>
  :root {
    --bg: #dcdcdc;
    --white: #ffffff;
    --mango: #f2b224;
    --mango-deep: #e4661d;
    --mango-badge: #ee6a24;
    --melon: #dc2d4a;
    --melon-green: #7b9a3e;
    --melon-badge: #6d8d35;
    --pine: #f6d02b;
    --pine-deep: #f0a21c;
    --pine-badge: #efb923;
    --ink-soft: rgba(255,255,255,0.95);
  }
  * { box-sizing: border-box; margin: 0; padding: 0; }
  html, body { width: 1200px; height: 912px; overflow: hidden; }
  body {
    background: linear-gradient(180deg, #e9e9e9 0%, var(--bg) 100%);
    font-family: "Montserrat", sans-serif;
  }
  .range {
    position: relative;
    width: 1200px; height: 912px;
  }
  .label {
    position: absolute;
    top: 150px;
    width: 220px; height: 600px;
    background: var(--white);
    overflow: hidden;
    border-radius: 6px;
  }
  .label--mango { left: 214px; --brand: var(--mango); --accent: var(--mango-deep); --top: var(--mango); --badge: var(--mango-badge); }
  .label--melon { left: 476px; --brand: var(--melon); --accent: var(--white); --top: var(--melon-green); --badge: var(--melon-badge); }
  .label--pine  { left: 738px; --brand: var(--pine); --accent: var(--pine-deep); --top: var(--pine); --badge: var(--pine-badge); }

  .top-band {
    position: absolute; left: 0; top: 0;
    width: 220px; height: 40px;
  }
  .top-band path { fill: var(--top); }

  .base {
    position: absolute; left: 0; top: 300px;
    width: 220px; height: 300px;
  }
  .base-wave { display: block; width: 220px; height: 20px; }
  .base-wave path { fill: var(--brand); }
  .base-fill { width: 220px; height: 280px; background: var(--brand); }

  .brand-name {
    position: absolute; left: 0; top: 88px; width: 220px;
    text-align: center;
    font-family: "Josefin Sans", sans-serif;
    font-weight: 700;
    font-size: 40px;
    letter-spacing: 1px;
    color: var(--brand);
  }
  .label--melon .brand-name { color: var(--melon); }

  .fruit {
    position: absolute; left: 30px; top: 172px;
    width: 160px; height: 200px;
    border-radius: 48% 52% 46% 54% / 50% 50% 50% 50%;
  }
  .label--mango .fruit { background: radial-gradient(circle at 50% 55%, #f7a826 0%, #f2b84a 55%, rgba(242,178,36,0.35) 80%, rgba(255,255,255,0) 100%); }
  .label--melon .fruit { background: radial-gradient(circle at 50% 50%, #f05a64 0%, #e23e50 50%, rgba(123,154,62,0.45) 78%, rgba(255,255,255,0) 100%); }
  .label--pine  .fruit { background: radial-gradient(circle at 55% 50%, #f6dc6a 0%, #e9c24a 50%, rgba(200,150,50,0.45) 78%, rgba(255,255,255,0) 100%); }

  .badge {
    position: absolute; left: 160px; top: 300px;
    width: 52px; height: 64px;
    border-radius: 50% 50% 50% 50% / 55% 55% 45% 45%;
    background: var(--badge);
    color: var(--white);
    font-family: "Fredoka", sans-serif;
    font-weight: 600;
    font-size: 10px;
    line-height: 11px;
    text-align: center;
    display: flex; align-items: center; justify-content: center;
  }

  .flavour {
    position: absolute; left: 0; width: 220px;
    text-align: center;
    font-family: "Federo", sans-serif;
    color: var(--white);
    line-height: 1;
  }
  .flavour-name { top: 402px; font-size: 46px; }
  .label--melon .flavour-name { font-size: 30px; top: 412px; }
  .label--pine .flavour-name { font-size: 33px; top: 408px; }
  .flavour-type {
    top: 452px; font-size: 30px; letter-spacing: 4px;
    color: var(--accent);
  }

  .claims {
    position: absolute; left: 18px; top: 505px;
    width: 184px; height: 32px;
    display: flex;
    border: 1px solid var(--ink-soft);
    color: var(--white);
  }
  .claim {
    flex: 1 1 auto;
    display: flex; flex-direction: column; justify-content: center; align-items: center;
    border-right: 1px solid var(--ink-soft);
    line-height: 1;
  }
  .claim:last-child { border-right: 0; }
  .claim small { font-size: 7px; font-weight: 500; letter-spacing: 0.3px; }
  .claim strong { font-size: 12px; font-weight: 600; }
  .claim--natural strong { order: -1; }

  .volume {
    position: absolute; left: 0; top: 560px; width: 220px;
    text-align: center;
    font-size: 12px; font-weight: 500;
    color: var(--white);
  }
</style>
</head>
<body>
<main class="range">

  <section class="label label--mango">
    <svg class="top-band" viewBox="0 0 220 40" preserveAspectRatio="none" aria-hidden="true"><path d="M0 0 H220 V30 Q213.1 38 206.25 30 T192.5 30 T178.75 30 T165 30 T151.25 30 T137.5 30 T123.75 30 T110 30 T96.25 30 T82.5 30 T68.75 30 T55 30 T41.25 30 T27.5 30 T13.75 30 T0 30 Z"/></svg>
    <div class="brand-name">Ma V's</div>
    <div class="base">
      <svg class="base-wave" viewBox="0 0 220 20" preserveAspectRatio="none" aria-hidden="true"><path d="M0 10 Q6.875 2 13.75 10 T27.5 10 T41.25 10 T55 10 T68.75 10 T82.5 10 T96.25 10 T110 10 T123.75 10 T137.5 10 T151.25 10 T165 10 T178.75 10 T192.5 10 T206.25 10 T220 10 V20 H0 Z"/></svg>
      <div class="base-fill"></div>
    </div>
    <div class="fruit" role="img" aria-label="Cubed mango half in a splash of juice"></div>
    <div class="badge">Made<br>From<br>Whole<br>Fruit</div>
    <div class="flavour flavour-name">MANGO</div>
    <div class="flavour flavour-type">JUICE</div>
    <div class="claims">
      <div class="claim claim--natural"><small>NATURAL</small><strong>100%</strong></div>
      <div class="claim"><small>NO ADDED</small><strong>SUGAR</strong></div>
      <div class="claim"><small>NEVER FROM</small><small>CONCENTRATE</small></div>
    </div>
    <div class="volume">500 ml</div>
  </section>

  <section class="label label--melon">
    <svg class="top-band" viewBox="0 0 220 40" preserveAspectRatio="none" aria-hidden="true"><path d="M0 0 H220 V30 Q213.1 38 206.25 30 T192.5 30 T178.75 30 T165 30 T151.25 30 T137.5 30 T123.75 30 T110 30 T96.25 30 T82.5 30 T68.75 30 T55 30 T41.25 30 T27.5 30 T13.75 30 T0 30 Z"/></svg>
    <div class="brand-name">Ma V's</div>
    <div class="base">
      <svg class="base-wave" viewBox="0 0 220 20" preserveAspectRatio="none" aria-hidden="true"><path d="M0 10 Q6.875 2 13.75 10 T27.5 10 T41.25 10 T55 10 T68.75 10 T82.5 10 T96.25 10 T110 10 T123.75 10 T137.5 10 T151.25 10 T165 10 T178.75 10 T192.5 10 T206.25 10 T220 10 V20 H0 Z"/></svg>
      <div class="base-fill"></div>
    </div>
    <div class="fruit" role="img" aria-label="Watermelon wedges with a red juice splash"></div>
    <div class="badge">Made<br>From<br>Whole<br>Fruit</div>
    <div class="flavour flavour-name">WATERMELON</div>
    <div class="flavour flavour-type">JUICE</div>
    <div class="claims">
      <div class="claim claim--natural"><small>NATURAL</small><strong>100%</strong></div>
      <div class="claim"><small>NO ADDED</small><strong>SUGAR</strong></div>
      <div class="claim"><small>NEVER FROM</small><small>CONCENTRATE</small></div>
    </div>
    <div class="volume">500 ml</div>
  </section>

  <section class="label label--pine">
    <svg class="top-band" viewBox="0 0 220 40" preserveAspectRatio="none" aria-hidden="true"><path d="M0 0 H220 V30 Q213.1 38 206.25 30 T192.5 30 T178.75 30 T165 30 T151.25 30 T137.5 30 T123.75 30 T110 30 T96.25 30 T82.5 30 T68.75 30 T55 30 T41.25 30 T27.5 30 T13.75 30 T0 30 Z"/></svg>
    <div class="brand-name">Ma V's</div>
    <div class="base">
      <svg class="base-wave" viewBox="0 0 220 20" preserveAspectRatio="none" aria-hidden="true"><path d="M0 10 Q6.875 2 13.75 10 T27.5 10 T41.25 10 T55 10 T68.75 10 T82.5 10 T96.25 10 T110 10 T123.75 10 T137.5 10 T151.25 10 T165 10 T178.75 10 T192.5 10 T206.25 10 T220 10 V20 H0 Z"/></svg>
      <div class="base-fill"></div>
    </div>
    <div class="fruit" role="img" aria-label="Stacked pineapple rings and a halved pineapple with juice splash"></div>
    <div class="badge">Made<br>From<br>Whole<br>Fruit</div>
    <div class="flavour flavour-name">PINEAPPLE</div>
    <div class="flavour flavour-type">JUICE</div>
    <div class="claims">
      <div class="claim claim--natural"><small>NATURAL</small><strong>100%</strong></div>
      <div class="claim"><small>NO ADDED</small><strong>SUGAR</strong></div>
      <div class="claim"><small>NEVER FROM</small><small>CONCENTRATE</small></div>
    </div>
    <div class="volume">500 ml</div>
  </section>

</main>
</body>
</html>
```